Modernise existing business card and letterhead designs

Based on the existing business card and letterhead design (in InDesign and Word formats respectively), I seek a new stationery design suite that has the following qualities:
For Business Cards:
* three colours only - blue (C=64, M=9, Y=0, K=0), grey and white
* two sided
* minimalist yet modern look
* retention of all text in AccordAlternate font
* retention of logo
* retention of QR code
* all else can be changed, including all the above in terms of size, location, and replacement of capital letter headers (eg address, telephone, fax, mobile, etc) with symbols
For Letterhead:
* single sided
* retention of logo
All files are available via https://www.filecrate.example/sh/k4pazr2mw9xq7tb/BBQxZr7pLmNvKeWtYuHsGfD3c?dl=0
The final output needs to be made available with the following requirements for download:
* business card template in at least Adobe InDesign CS3 version 5.0 format
* letterhead template in Word format, with associated files in EPS and JPEG embedded
* associated files in EPS and JPEG
* files of the fonts used
Target Market(s)
- Young entrepreneurs and business owners
- legislators and government bureaucrats
Industry/Entity Type
Leadership
Requirements
Must have
- - Use of logo, corporate font and corporate colour (C=64, M=9, Y=0, K=0)
- - as minimalistic as possible
- - modern look
- - retention of the (85 mm x 55 mm) dimensions of the business card design
- - retention of the A4 dimensions of the letterhead design
Nice to have
- - use of symbols instead of text wherever possible (eg capital letter titles for address, telephone, fax, mobile, e-mail, website, etc)
Should not have
- - avoid being too traditional

```html
<!DOCTYPE html>
<html lang="en">
<head>
<meta charset="utf-8">
<title>Letterhead – Southern Kinder Collective</title>
<link rel="stylesheet" href="https://fonts.googleapis.com/css2?family=Mulish:wght@300;400;600;700&display=swap">
<style>
  :root {
    --brand-blue: #29abe2;
    --ink: #2b2b2b;
    --ink-soft: #4a4a4a;
    --paper: #ffffff;
    --backdrop: #e6e6e6;
  }
  * { margin: 0; padding: 0; box-sizing: border-box; }
  html, body { width: 1200px; height: 1200px; overflow: hidden; }
  body {
    background: var(--backdrop);
    font-family: "Mulish", Arial, sans-serif;
    color: var(--ink);
    position: relative;
  }
  .letterhead {
    position: absolute;
    left: 211px; top: 50px;
    width: 778px; height: 1100px;
    background: var(--paper);
    box-shadow: 0 4px 18px rgba(0,0,0,0.12);
  }
  .brand {
    position: absolute;
    left: 92px; top: 96px;
    display: flex; align-items: center; gap: 12px;
  }
  .brand-square {
    width: 44px; height: 44px;
    background: var(--brand-blue);
  }
  .brand-name {
    font-weight: 600;
    font-size: 16px;
    line-height: 1.15;
    color: var(--ink);
  }
  .brand-name small { display: block; font-size: 13px; }
  .letter-body {
    position: absolute;
    left: 110px; top: 318px;
    width: 540px;
    font-size: 13.5px;
    line-height: 1.72;
    font-weight: 400;
    color: var(--ink-soft);
  }
  .salutation { font-weight: 600; color: var(--ink); margin-bottom: 14px; }
  .letter-body p + p { margin-top: 24px; }
  .sign-off { position: absolute; left: 110px; top: 778px; }
  .signature-mark {
    width: 110px; height: 56px;
    background: linear-gradient(135deg, #f2f2f2, #e4e4e4);
    border-radius: 4px;
  }
  .signer-name { margin-top: 12px; font-size: 21px; font-weight: 400; color: var(--ink); }
  .signer-role { font-size: 15px; font-weight: 300; color: var(--ink-soft); margin-top: 2px; }
  .contact-footer {
    position: absolute;
    right: 60px; bottom: 70px;
    font-size: 10.5px;
    line-height: 1.7;
    color: var(--ink-soft);
    text-align: left;
  }
  .contact-org { color: var(--brand-blue); font-size: 13px; font-weight: 400; margin-bottom: 2px; }
  .contact-line { display: flex; align-items: center; gap: 10px; white-space: nowrap; }
  .contact-item { display: inline-flex; align-items: center; gap: 4px; }
  .contact-item svg { width: 10px; height: 10px; fill: var(--brand-blue); flex: none; }
</style>
</head>
<body>
  <main class="letterhead">
    <header class="brand">
      <span class="brand-square"></span>
      <div class="brand-name">Southern Kinder Collective<small>Coastal Region</small></div>
    </header>

    <section class="letter-body">
      <p class="salutation">Dear Mr. Smith,</p>
      <p>Lorem ipsum dolor sit amet, consectetur adipiscing elit. Donec orci purus, luctus vitae dignissim eu, iaculis sed purus. Vivamus faucibus, ipsum nec aliquet viverra, leo mauris condimentum ligula, sit amet sagittis enim ligula quis arcu. Nam egestas tortor id nisi porttitor mattis. In tortor ante, ultricies in suscipit a, tempus non massa. Vivamus et auctor mi. Fusce vel massa nulla. Phasellus nec eros mauris, et scelerisque orci. Donec malesuada orci vitae nulla accumsan porta a id massa. Quisque accumsan iaculis magna sit amet fringilla. Maecenas consequat, magna eget tincidunt semper, odio nibh rutrum mi, id feugiat ante nisi eu risus. Vestibulum nunc orci, rhoncus a placerat in, ultricies in mi. Cras mattis varius eros, vel fringilla nisi suscipit eget.</p>
      <p>Quisque scelerisque sagittis nulla at porttitor. Mauris a justo et tellus interdum tristique. Sed id augue vitae urna euismod commodo aliquet a quam. Pellentesque arcu velit, cursus et malesuada ut, consequat et diam. Nullam erat sem, rhoncus id ullamcorper vitae, rhoncus et arcu. In ultricies ultricies nulla, ut rutrum nisi iaculis at. Donec eu magna a metus ornare faucibus. Fusce aliquet faucibus ultricies. Morbi semper, est id tincidunt gravida, sem arcu adipiscing lacus, ac bibendum nulla leo eu purus. Quisque nec diam sed risus consectetur accumsan quis quis nibh. Vestibulum id purus lorem.</p>
    </section>

    <section class="sign-off">
      <div class="signature-mark" role="img" aria-label="Handwritten signature of John Doe"></div>
      <p class="signer-name">John Doe</p>
      <p class="signer-role">Co-Founder &amp; CEO</p>
    </section>

    <footer class="contact-footer">
      <p class="contact-org">Southern Kinder Collective Coastal Region</p>
      <div class="contact-line">
        <span class="contact-item"><svg viewBox="0 0 10 10"><path d="M5 0a3.5 3.5 0 0 0-3.5 3.5C1.5 6 5 10 5 10s3.5-4 3.5-6.5A3.5 3.5 0 0 0 5 0zm0 5a1.5 1.5 0 1 1 0-3 1.5 1.5 0 0 1 0 3z"/></svg>PO Box 418, Millbrook 2150</span>
        <span class="contact-item"><svg viewBox="0 0 10 10"><path d="M2 0h2l.8 2.4-1.3 1a6 6 0 0 0 2.6 2.6l1-1.3L9.5 5.5V8a1.5 1.5 0 0 1-1.5 1.5C3.8 9.5.5 6.2.5 2A1.5 1.5 0 0 1 2 0z"/></svg>1300 482 615</span>
        <span class="contact-item"><svg viewBox="0 0 10 10"><path d="M3 0h4a1 1 0 0 1 1 1v8a1 1 0 0 1-1 1H3a1 1 0 0 1-1-1V1a1 1 0 0 1 1-1zm0 1.5v6h4v-6z"/></svg>0400 118 274</span>
        <span class="contact-item"><svg viewBox="0 0 10 10"><path d="M2.5 0h5v3h-5zM1 3.5h8a1 1 0 0 1 1 1V8H8v2H2V8H0V4.5a1 1 0 0 1 1-1zm2 4.5v1h4V8z"/></svg>1300 482 616</span>
      </div>
      <div class="contact-line">
        <span class="contact-item"><svg viewBox="0 0 10 10"><path d="M0 2h10v6H0zm1 .8v.4l4 2.6 4-2.6v-.4L5 5z"/></svg>m.tran@kindercollective.example</span>
        <span class="contact-item"><svg viewBox="0 0 10 10"><path d="M5 0a5 5 0 1 0 0 10A5 5 0 0 0 5 0zm0 1c.6 0 1.3 1.3 1.5 3.5h-3C3.7 2.3 4.4 1 5 1zM3.5 5.5h3C6.3 7.7 5.6 9 5 9s-1.3-1.3-1.5-3.5zM1 5.5h1.5c.1 1.2.3 2.2.7 2.9A4 4 0 0 1 1 5.5zm6.5 0H9a4 4 0 0 1-2.2 2.9c.4-.7.6-1.7.7-2.9zM1 4.5a4 4 0 0 1 2.2-2.9c-.4.7-.6 1.7-.7 2.9zm6.5 0c-.1-1.2-.3-2.2-.7-2.9A4 4 0 0 1 9 4.5z"/></svg>www.kindercollective.example</span>
      </div>
    </footer>
  </main>
</body>
</html>
```